New Website for Belcourt Manor at www.belcourt.com.au

A new logo has been designed (through pixel forge) and we now want to align the look and feel of our website at www.belcourt.com.au to the new logo. The content and page names (e.g. Grounds) will remain largely unchanged for the new site, so please submit a new look "Home" page, using our new logo, current text and any photos you choose from the existing gallery at our website. I have also attached the current "Home" page photos.

Industry/Entity Type

Accommodation

Number of Pages Required

1 page

Requirements
Must have
• Logo to be presented on white background.

```html
<!DOCTYPE html>
<html lang="en">
<head>
<meta charset="utf-8">
<title>Belcourt Manor – Home</title>
<link href="https://fonts.googleapis.com/css2?family=Roboto:wght@300;400;500;700&display=swap" rel="stylesheet">
<style>
:root{
  --blue:#1b93d8;
  --yellow:#f4d535;
  --ink:#2b2b2b;
  --text:#444;
  --muted:#8a8a8a;
  --page:#ffffff;
  --backdrop:#e9e9e9;
  --pale:#f1f1f1;
  --dark:#1d1d1d;
  --footer:#232323;
  --field:#2f2f2f;
}
*{margin:0;padding:0;box-sizing:border-box}
html,body{width:1200px;height:3377px;overflow:hidden}
body{background:var(--backdrop);font-family:'Roboto',Arial,sans-serif;color:var(--text);position:relative}
.page{position:absolute;left:61px;top:0;width:1078px;height:2998px;background:var(--page)}
.abs{position:absolute}
.center{text-align:center;left:0;right:0}

/* brand */
.brand{display:flex;align-items:center;gap:10px;font-weight:500;color:var(--blue);letter-spacing:.5px}
.brand .sun{border-radius:50%;background:var(--yellow);flex:none}
.header-brand{left:0;right:0;top:30px;justify-content:center;font-size:44px}
.header-brand .sun{width:40px;height:40px}
.social{display:flex;gap:10px}
.social span{width:26px;height:26px;border-radius:50%;background:#bdbdbd;display:block}
.header-social{left:912px;top:56px}

/* nav */
.nav{left:56px;width:966px;top:117px;border-top:3px solid #e3e3e3;display:flex;justify-content:space-between;padding:8px 10px 0;font-size:11.5px;color:#8d8d8d;letter-spacing:.3px}
.nav .active{color:var(--blue)}

/* hero */
.hero{left:56px;top:146px;width:966px;height:428px;background:linear-gradient(180deg,#3f6b3a 0%,#5d8b4c 18%,#c9582f 34%,#e0b94f 52%,#d7b45a 68%,#8d8a7d 82%,#6f6e68 100%)}
.hero-title{left:88px;top:412px;color:#fff;font-weight:700;font-size:60px;line-height:1;letter-spacing:1px}
.hero-sub{left:88px;top:474px;color:#fff;font-weight:300;font-size:30px;letter-spacing:1px}

/* welcome */
.kicker{font-weight:300;font-size:20px;color:#666}
.headline{font-size:34px;color:var(--ink);font-weight:300;letter-spacing:1px}
.headline b{font-weight:700}
.tagline{font-size:13px;color:#333}
.body-copy{font-size:13px;line-height:25px;color:#555;margin:0 auto}
.rule{height:2px;background:#e5e5e5}

.photo{background:#ccc}
.interior-left{left:0;top:806px;width:677px;height:403px;background:linear-gradient(180deg,#f3eee4 0%,#e9dcc6 40%,#8c7a64 62%,#3b3632 76%,#b86a3f 100%)}
.interior-right{left:677px;top:806px;width:401px;height:403px;background:linear-gradient(180deg,#f1e9d6 0%,#e8d7b2 40%,#b57848 62%,#5a8fa3 80%,#c99366 100%)}

/* rooms */
.headline .accent{color:var(--yellow);font-weight:700}
.room{width:210px;height:300px;border:1px solid #e4e4e4;background:#fff;padding:7px}
.room .shot{height:250px;background:linear-gradient(180deg,#f3efe6 0%,#e4d9c5 45%,#b89e7c 70%,#6c5a46 100%)}
.room .label{font-size:19px;font-weight:300;color:#555;text-align:center;margin-top:8px;white-space:nowrap}
.room .label b{font-weight:700;color:#333}
.btn-view{left:470px;top:1794px;width:138px;height:23px;background:var(--yellow);color:#444;font-size:13px;text-align:center;line-height:23px}

/* pub */
.pub-panel{left:0;top:1895px;width:416px;height:433px;background:var(--dark)}
.pub-bar{left:34px;top:1895px;width:348px;height:6px;background:var(--blue)}
.pub-photo{left:416px;top:1895px;width:662px;height:433px;background:linear-gradient(160deg,#0f1f4a 0%,#1c3a7a 35%,#3b4a4f 55%,#c79a5c 75%,#e9c27c 100%)}
.pub-kicker{left:52px;top:2016px;color:#fff;font-weight:300;font-size:19px}
.pub-title{left:52px;top:2041px;color:var(--blue);font-size:34px;font-weight:400;letter-spacing:.5px}
.pub-lead{left:52px;top:2084px;color:#fff;font-size:12px;font-weight:700}
.pub-copy{left:52px;top:2114px;width:300px;color:#ddd;font-size:12.5px;line-height:23px}

/* testimonial */
.quote-band{left:0;top:2328px;width:1078px;height:310px;background:var(--pale)}
.quote-icon{width:28px;height:28px;border-radius:50%;background:#b5b5b5;color:#fff;font-size:26px;line-height:34px;text-align:center;font-weight:700;left:525px}
.quote-head{font-size:16px;color:#333}
.quote-line{font-size:14px;color:#444}
.quote-by{font-size:15px;color:#444}
.quote-by b{color:#222}
.quote-bar{left:391px;top:2634px;width:296px;height:7px;background:var(--blue)}

/* closing */
.closing-brand{left:0;right:0;top:2722px;justify-content:center;font-size:48px}
.closing-brand .sun{width:44px;height:44px}
.closing-title{top:2812px;font-size:66px;font-weight:700;color:#3a3a3a;letter-spacing:1px}
.closing-sub{top:2888px;font-size:36px;font-weight:300;color:#444;letter-spacing:1px}
.closing-rule{left:294px;top:2936px;width:490px;height:2px;background:#d9d9d9}

/* footer */
.footer{position:absolute;left:0;top:2998px;width:1200px;height:379px;background:var(--footer)}
.contact-title{left:124px;top:45px;color:#fff;font-size:32px;font-weight:300;line-height:34px}
.contact-title b{font-weight:700}
.contact-note{left:124px;top:122px;width:190px;color:#fff;font-size:10px;line-height:14px}
.field{background:var(--field);color:#777;font-size:10px;padding:4px 10px}
.field-mail{left:124px;top:160px;width:175px;height:20px}
.field-query{left:124px;top:183px;width:175px;height:92px}
.field-code{left:124px;top:278px;width:92px;height:20px}
.captcha{left:218px;top:278px;width:81px;height:20px;background:#101010;color:#eee;font-size:11px;letter-spacing:1px;text-align:center;line-height:20px}
.submit{left:180px;top:315px;width:70px;height:23px;background:#3a3a3a;color:#aaa;font-size:12px;text-align:center;line-height:23px}
.round-icon{width:30px;height:30px;border-radius:50%;background:#e6e6e6;display:flex;align-items:center;justify-content:center;left:518px}
.contact-lines{left:400px;width:266px;text-align:center;color:#9a9a9a;font-size:16px;line-height:28px;letter-spacing:.5px}
.map{left:732px;top:138px;width:405px;height:142px;background:linear-gradient(135deg,#cfcfcf 0%,#bdbdbd 50%,#a9a9a9 100%)}
.map-card{left:1019px;top:138px;width:118px;height:142px;background:#3a3a3a;padding:7px}
.map-card .logo-box{background:#fff;height:66px;display:flex;align-items:center;justify-content:center;gap:4px;font-size:15px;color:var(--blue);font-weight:500}
.map-card .logo-box i{width:12px;height:12px;border-radius:50%;background:var(--yellow);display:block}
.map-card p{color:#ddd;font-size:9.5px;line-height:13px;margin-top:8px}
.footer-social{left:1028px;top:315px}
.footer-social span{background:#9a9a9a}
</style>
</head>
<body>
<div class="page">
  <!-- header -->
  <div class="abs brand header-brand"><span class="sun"></span>Belcourt</div>
  <div class="abs social header-social"><span></span><span></span><span></span></div>
  <nav class="abs nav">
    <span class="active">MAIN</span><span>MANSION</span><span>BEDROOMS</span><span>OPTIONS</span><span>OWL &amp; WREN</span><span>GROUNDS</span><span>LOCATION</span><span>GALLERY</span><span>CONTACT</span><span>AVAILABILITY</span><span>DIY WEDDINGS</span>
  </nav>

  <!-- hero -->
  <div class="abs hero" role="img" aria-label="Photo of the manor: yellow house with terracotta roof among tropical gardens"></div>
  <div class="abs hero-title">EXPERIENCE</div>
  <div class="abs hero-sub">THE LUXURY</div>

  <!-- welcome -->
  <div class="abs center kicker" style="top:605px;text-align:center">Welcome to</div>
  <div class="abs center headline" style="top:628px;text-align:center"><b>BELCOURT</b> MANOR</div>
  <div class="abs center tagline" style="top:673px;text-align:center">One of australia's most loved Palatial Estate &amp; Luxury Resort.</div>
  <p class="abs body-copy" style="left:290px;top:708px;width:498px;text-align:center">On over 2 manicured garden acres, this unique Gold Coast estate is located in the prestigious rural suburb of Ridgevale and features a grand mansion, pub, sparkling resort pool, tennis court, playground and more!</p>
  <div class="abs rule" style="left:475px;top:796px;width:128px"></div>

  <div class="abs interior-left" role="img" aria-label="Photo of the grand living room with leather sofas and a fireplace"></div>
  <div class="abs interior-right" role="img" aria-label="Photo of the curved staircase with carpeted steps"></div>

  <!-- rooms -->
  <div class="abs center kicker" style="top:1258px;text-align:center">Indulge yourself in</div>
  <div class="abs center headline" style="top:1280px;text-align:center"><span class="accent">LUXURIOUS</span> ROOMS</div>
  <div class="abs center tagline" style="top:1326px;text-align:center">Experience comfort with style!</div>
  <p class="abs body-copy" style="left:290px;top:1360px;width:498px;text-align:center">The Resort has a total of # luxurious rooms in the classic style that cater to the modern traveler's every need. A variety of room categories makes it possible for the guest to select that combination that most suits the purpose of their visit.</p>

  <div class="abs room" style="left:205px;top:1463px"><div class="shot" role="img" aria-label="Photo of the king bedroom"></div><div class="label">01. <b>KING</b> SUIT</div></div>
  <div class="abs room" style="left:434px;top:1463px"><div class="shot" role="img" aria-label="Photo of the balcony bedroom"></div><div class="label">02. <b>BALCONY</b> SUIT</div></div>
  <div class="abs room" style="left:664px;top:1463px"><div class="shot" role="img" aria-label="Photo of the queens bedroom"></div><div class="label">03. <b>QUEENS</b> SUIT</div></div>
  <div class="abs btn-view">VIEW ALL</div>

  <!-- pub -->
  <div class="abs pub-panel"></div>
  <div class="abs pub-bar"></div>
  <div class="abs pub-photo" role="img" aria-label="Photo of the private pub at dusk with a timber deck and open bi-fold doors"></div>
  <div class="abs pub-kicker">your own private pub</div>
  <div class="abs pub-title">THE OWL &amp; WREN</div>
  <div class="abs pub-lead">Day or night, enjoy a quiet one in your pub</div>
  <p class="abs pub-copy">The Owl and Wren is a stand-alone, 83 square metre building with sliding bi-fold doors that open to a huge timber deck; fully covered by retractable awnings.</p>

  <!-- testimonial -->
  <div class="abs quote-band"></div>
  <div class="abs quote-icon" style="top:2370px">&ldquo;</div>
  <div class="abs center quote-head" style="top:2419px;text-align:center">Exceeds all expectations!</div>
  <div class="abs center quote-line" style="top:2451px;text-align:center">Perfect location for a small wedding. The property and grounds were spectacular!</div>
  <div class="abs center quote-line" style="top:2483px;text-align:center">Thank you Helen &amp; Mark you always make our stay so amazing!!</div>
  <div class="abs quote-icon" style="top:2525px">&rdquo;</div>
  <div class="abs center quote-by" style="top:2573px;text-align:center"><b>Tessa</b>, Australia</div>
  <div class="abs quote-bar"></div>

  <!-- closing -->
  <div class="abs brand closing-brand"><span class="sun"></span>Belcourt</div>
  <div class="abs center closing-title" style="text-align:center">EXPERIENCE</div>
  <div class="abs center closing-sub" style="text-align:center">MORE THAN YOU CAN IMAGINE</div>
  <div class="abs closing-rule"></div>
</div>

<footer class="footer">
  <div class="abs contact-title">CONTACT<br><b>US!</b></div>
  <p class="abs contact-note">We look forward to having you as our guests at Belcourt Manor</p>
  <div class="abs field field-mail">Your mail ID*</div>
  <div class="abs field field-query">Query</div>
  <div class="abs field field-code">Enter Code</div>
  <div class="abs captcha">K7Q2X9</div>
  <div class="abs submit">Submit</div>

  <div class="abs round-icon" style="top:91px">
    <svg width="16" height="12" viewBox="0 0 16 12"><rect x="0.5" y="0.5" width="15" height="11" fill="#232323"/><path d="M1 1l7 6 7-6" stroke="#e6e6e6" stroke-width="1.4" fill="none"/></svg>
  </div>
  <div class="abs contact-lines" style="top:130px">kb@belcourt.com.au<br>gb@belcourt.com.au</div>
  <div class="abs round-icon" style="top:213px">
    <svg width="16" height="16" viewBox="0 0 24 24"><path d="M6.6 10.8a15.1 15.1 0 006.6 6.6l2.2-2.2a1 1 0 011-.25 11.4 11.4 0 003.6.57 1 1 0 011 1V20a1 1 0 01-1 1A17 17 0 013 4a1 1 0 011-1h3.5a1 1 0 011 1 11.4 11.4 0 00.57 3.6 1 1 0 01-.25 1z" fill="#232323"/></svg>
  </div>
  <div class="abs contact-lines" style="top:258px;line-height:30px;font-size:17px">0400 555 218<br>0400 555 364<br>1300 555 709</div>

  <div class="abs map" role="img" aria-label="Street map showing the location of the manor"></div>
  <div class="abs map-card">
    <div class="logo-box"><i></i>Belcourt</div>
    <p>19 Belcourt Drive<br>Ridgevale,<br>Queensland, Australia</p>
  </div>
  <div class="abs social footer-social"><span></span><span></span><span></span></div>
</footer>
</body>
</html>
```